Bright Leaf Bistro & Pantry Squarespace Website Files

We need a Squarespace website for a new company called "Bright Leaf Bistro & Pantry".

The company is committed to providing the highest quality, fresh and natural food, health and wellness products.

We would like to see designs that use the colors of our logo. Please provide graphic design and layout for the site.

The final design should communicate health and wellness.

Target Market(s)

Bright Leaf Bistro & Pantry is a new company that will offer customers organic and
locally grown produce, chemical and preservative-free groceries, cruelty-free body care and eco-household products. Additionally, our kitchen will offer healthy lunch and dinner options emphasizing organic and whole food options, recognizing the trend within the restaurant industry for the demand for healthy cuisine. The restaurant will procure local foods when possible, reducing dependence on fossil fuels used for transportation. All of our products are healthy alternatives to the products available at conventional grocery chains.

Located in the heart of the growing Harlow Street section of Lewiston, NY, the
marketplace will serve a community of residents in Lewiston, residents in
Niagara Falls, and residents in Niagara Falls, Ontario, Canada.

The creation of the marketplace is in response to the growing demand in the community for a local natural food store.

Industry/Entity Type

Cafe

Font styles to use
Sans Serif

Colors
00a990
faa54b
87cfc7
f37122

Requirements
Must have
• Home page, Events, Cafe Menu, Marketplace Products, Health Info, News, Recipes, Contact Us (Email form and Social Media links), Newsletter sign up.
Nice to have
• Order Online
Should not have
• (Can't think of anything right now :-)

```html
<!DOCTYPE html>
<html lang="en">
<head>
<meta charset="utf-8">
<title>Bright Leaf Bistro &amp; Pantry</title>
<link rel="stylesheet" href="https://fonts.googleapis.com/css2?family=Montserrat:wght@400;500;600&family=Noto+Serif:wght@700&family=Arimo:wght@400&display=swap">
<style>
  :root {
    --teal: #00a990;
    --teal-light: #87cfc7;
    --orange-soft: #faa54b;
    --orange: #f37122;
    --ink: #111111;
    --heading: #1f3a33;
    --muted: #555555;
    --nav-small: #777777;
    --panel: #e4f3f1;
    --stone: #8a8a82;
    --white: #ffffff;
  }
  * { box-sizing: border-box; margin: 0; padding: 0; }
  html, body { width: 1200px; height: 1190px; overflow: hidden; }
  body { font-family: "Montserrat", sans-serif; background: var(--stone); position: relative; color: var(--ink); }

  .site-header { position: absolute; left: 0; top: 0; width: 1200px; height: 151px; background: var(--white); }
  .brand { position: absolute; left: 105px; top: 54px; display: flex; align-items: center; gap: 12px; font-size: 28px; font-weight: 600; color: var(--teal); }
  .brand-dot { width: 20px; height: 20px; border-radius: 50%; background: var(--orange-soft); }
  .utility-nav { position: absolute; right: 130px; top: 31px; font-size: 11.5px; font-weight: 500; color: var(--nav-small); }
  .utility-nav span { margin: 0 5px; }
  .main-nav { position: absolute; right: 125px; top: 72px; display: flex; gap: 22px; font-size: 16px; font-weight: 500; }
  .main-nav a, .utility-nav a { color: inherit; text-decoration: none; }

  .hero { position: absolute; left: 0; top: 151px; width: 1200px; height: 425px;
    background:
      radial-gradient(circle at 8% 25%, #c8281e 0 9%, transparent 16%),
      radial-gradient(circle at 62% 45%, #c1201b 0 10%, transparent 20%),
      radial-gradient(circle at 88% 30%, #8b1b24 0 8%, transparent 17%),
      radial-gradient(circle at 72% 10%, #e9c531 0 6%, transparent 13%),
      radial-gradient(circle at 82% 80%, #e9e2d0 0 7%, transparent 14%),
      radial-gradient(circle at 58% 85%, #b88a4e 0 10%, transparent 20%),
      radial-gradient(circle at 35% 20%, #4f8a2a 0 14%, transparent 28%),
      linear-gradient(90deg, #e8ded2 0%, #c9b79e 40%, #7f9a45 70%, #a04a2e 100%); }
  .hero-card { position: absolute; left: 151px; top: 101px; width: 512px; height: 233px; background: rgba(245, 246, 240, 0.86); padding: 32px 34px; }
  .hero-card h1 { font-size: 42px; font-weight: 500; line-height: 42px; color: var(--heading); }
  .btn { display: inline-flex; align-items: center; justify-content: center; border-radius: 5px; text-decoration: none; font-weight: 500; }
  .btn-learn { position: absolute; left: 34px; top: 135px; width: 181px; height: 48px; background: var(--teal); color: var(--white); font-size: 19px; font-weight: 600; letter-spacing: 0.5px; }

  .content { position: absolute; left: 58px; top: 576px; width: 1074px; height: 517px; background: var(--white); }
  .feature { position: absolute; top: 33px; width: 237px; text-align: center; }
  .feature-photo { width: 237px; height: 155px; }
  .feature h2 { margin-top: 14px; font-size: 17px; font-weight: 600; color: var(--orange); }
  .feature p { margin-top: 20px; font-size: 11.5px; font-weight: 600; line-height: 16px; color: var(--muted); padding: 0 12px; }
  .photo-rice { background: radial-gradient(circle at 40% 55%, #e9d8a8 0 35%, #7a5b2a 60%, #222 100%); }
  .photo-lunch { background: radial-gradient(circle at 45% 55%, #d99a3a 0 20%, #f3f1ea 40%, #e4e2dc 100%); }
  .photo-curry { background: radial-gradient(circle at 50% 50%, #e07a2a 0 32%, #1d1a17 50%, #7a6a4a 100%); }

  .app-promo { position: absolute; left: 815px; top: 30px; width: 235px; height: 287px; background: var(--teal); text-align: center; }
  .app-promo h3 { margin-top: 10px; font-size: 21px; font-weight: 500; color: var(--white); }
  .phone { position: absolute; left: 55px; top: 52px; }
  .phone-label { position: absolute; left: 0; width: 235px; top: 147px; font-size: 12px; font-weight: 600; color: var(--teal); }
  .btn-download { position: absolute; left: 29px; top: 211px; width: 176px; height: 53px; background: var(--orange-soft); color: var(--ink); font-size: 17px; }

  .coupon-bar { position: absolute; left: 23px; top: 364px; width: 765px; height: 103px; background: var(--panel); }
  .coupon-bar label { position: absolute; left: 21px; top: 42px; font-family: "Noto Serif", serif; font-weight: 700; font-size: 17px; color: var(--teal); }
  .coupon-input { position: absolute; left: 174px; top: 33px; width: 272px; height: 45px; border-radius: 6px; background: var(--white); border: 1px solid var(--teal-light); font-size: 16px; color: #888; padding: 11px 13px; }
  .btn-signup { position: absolute; left: 462px; top: 36px; width: 129px; height: 42px; background: var(--teal); color: var(--white); font-size: 17px; }
  .btn-locations { position: absolute; left: 844px; top: 367px; width: 176px; height: 82px; background: var(--orange-soft); color: var(--ink); font-size: 17px; line-height: 23px; text-align: center; }

  .site-footer { position: absolute; left: 102px; top: 1115px; font-family: "Arimo", sans-serif; font-size: 12.5px; color: var(--white); line-height: 21px; }
  .social { position: absolute; right: 66px; top: 1126px; display: flex; gap: 24px; }
  .social span { width: 18px; height: 18px; border-radius: 50%; border: 2px solid #d8d8d2; }
</style>
</head>
<body>
  <header class="site-header">
    <div class="brand"><span class="brand-dot"></span>Bright Leaf Bistro &amp; Pantry</div>
    <nav class="utility-nav"><a href="#">News</a><span>I</span><a href="#">Recipes</a><span>I</span><a href="#">Contact Us</a></nav>
    <nav class="main-nav"><a href="#">Home</a><a href="#">About</a><a href="#">Events</a><a href="#">Cafe</a><a href="#">Products</a><a href="#">Health Info</a></nav>
  </header>

  <section class="hero" role="img" aria-label="Close-up of fresh tomatoes, peppers, onions, garlic and greens in a basket">
    <div class="hero-card">
      <h1>Organic and locally grown produce</h1>
      <a class="btn btn-learn" href="#">LEARN MORE</a>
    </div>
  </section>

  <main class="content">
    <article class="feature" style="left:27px">
      <div class="feature-photo photo-rice" role="img" aria-label="Shrimp fried rice with chopsticks"></div>
      <h2>Fresh Food</h2>
      <p>Every dish starts with organic, whole ingredients picked at their best. No preservatives, no shortcuts, just honest food made fresh in our kitchen each day.</p>
    </article>
    <article class="feature" style="left:294px">
      <div class="feature-photo photo-lunch" role="img" aria-label="Chicken curry over white rice on a square plate"></div>
      <h2>healthy lunch</h2>
      <p>Stop by for a nourishing lunch or dinner. Our cafe menu features hearty bowls, fresh salads and seasonal plates. Browse the full Cafe Menu.</p>
    </article>
    <article class="feature" style="left:544px">
      <div class="feature-photo photo-curry" role="img" aria-label="Bowl of vegetable curry with chopsticks"></div>
      <h2>local foods</h2>
      <p>We buy from nearby farms whenever we can, cutting transport and supporting growers across Lewiston and Niagara. Fresher food, a smaller footprint.</p>
    </article>

    <aside class="app-promo">
      <h3>Download our App</h3>
      <svg class="phone" width="125" height="170" viewBox="0 0 125 170" aria-hidden="true">
        <rect x="4" y="0" width="117" height="170" rx="14" fill="#1c1c1c"/>
        <rect x="12" y="22" width="101" height="148" fill="#ffffff"/>
      </svg>
      <div class="phone-label">Bright Leaf</div>
      <a class="btn btn-download" href="#">Download now</a>
    </aside>

    <form class="coupon-bar">
      <label>Want coupons?</label>
      <div class="coupon-input">your email</div>
      <a class="btn btn-signup" href="#">Sign up</a>
    </form>

    <a class="btn btn-locations" href="#">Find our<br>Locations</a>
  </main>

  <footer class="site-footer">
    <div>© 2015 Bright Leaf</div>
    <div>Home - Site Map – FAQ – Privacy Policy – Terms of Use – Contact Us</div>
  </footer>
  <div class="social" aria-label="Social links"><span></span><span></span><span></span><span></span></div>
</body>
</html>
```